negative postcard for political campaign

want a postcard just like the video. here is the video
http://clipvu.test/Rk42XbNq7Pz
here is a copy of the verbage on the video. photos will be attached
Is Mara Quill really what the Halverton School District needs?
In 2008, her son brought a gun to school.
Her Husband, Simon Quill while on the school board, said it was an honest mistake and nothing was ever done to the child.
If it were anyone else's child, that child would have been expelled.
Recently her son was arrested TWICE in 1 week for theft.
Is this the type of person you want on your school board?
If Mara Quill cant keep her own child out of trouble, how will she ever help your children?

```html
<!DOCTYPE html>
<html lang="en">
<head>
<meta charset="utf-8">
<title>Is Mara Quill really what the Halverton School District needs?</title>
<link rel="stylesheet" href="https://fonts.googleapis.com/css2?family=Questrial&family=Arimo:wght@400;700&display=swap">
<style>
  :root {
    --paper: #d8d2d2;
    --frame: #ffffff;
    --panel: #d3cdcd;
    --red: #e5232b;
    --ink: #333333;
    --hero-side: #cdc6c5;
    --hero-metal: #a9a09f;
    --hero-hair: #8a7160;
    --hero-skin: #caa48c;
    --hero-jacket: #1f1b1d;
    --hero-blouse: #c0457a;
  }
  * { box-sizing: border-box; margin: 0; padding: 0; }
  html, body { width: 1200px; height: 930px; overflow: hidden; background: var(--paper); }
  .postcard { position: relative; width: 1200px; height: 930px; background: var(--paper); }
  .frame {
    position: absolute; left: 29px; top: 29px; width: 1142px; height: 872px;
    background: var(--frame);
  }
  .hero {
    position: absolute; left: 32px; top: 32px; width: 1136px; height: 512px;
    background:
      radial-gradient(ellipse 150px 150px at 50% 46%, var(--hero-skin) 0%, rgba(202,164,140,0.85) 45%, rgba(202,164,140,0) 100%),
      radial-gradient(ellipse 230px 300px at 50% 40%, var(--hero-hair) 0%, rgba(138,113,96,0.6) 55%, rgba(138,113,96,0) 100%),
      radial-gradient(ellipse 80px 150px at 50% 100%, var(--hero-blouse) 0%, rgba(192,69,122,0) 100%),
      radial-gradient(ellipse 300px 230px at 50% 100%, var(--hero-jacket) 0%, rgba(31,27,29,0.85) 55%, rgba(31,27,29,0) 100%),
      radial-gradient(ellipse 280px 260px at 24% 45%, var(--hero-metal) 0%, rgba(169,160,159,0) 100%),
      radial-gradient(ellipse 280px 260px at 76% 45%, var(--hero-metal) 0%, rgba(169,160,159,0) 100%),
      var(--hero-side);
  }
  .headline {
    position: absolute; left: 32px; top: 544px; width: 1136px; height: 76px;
    display: flex; align-items: center; justify-content: center;
    font-family: "Questrial", sans-serif; font-size: 29px; color: var(--ink);
    letter-spacing: -0.5px; text-transform: uppercase; white-space: nowrap;
  }
  .headline .name { color: var(--red); font-size: 34px; padding: 0 6px; }
  .details {
    position: absolute; left: 32px; top: 620px; width: 1136px; height: 243px;
    background: var(--panel);
  }
  .mugshot, .husband-photo {
    position: absolute; top: 12px; width: 206px; height: 231px;
  }
  .mugshot { left: 65px; background: linear-gradient(180deg, #f2f0ee 0%, #c9a88e 60%, #e8e4e2 100%); }
  .husband-photo { left: 862px; background: linear-gradient(180deg, #c9d3dc 0%, #a98a76 55%, #8ea08a 100%); }
  .story {
    position: absolute; left: 243px; top: 18px; width: 650px;
    font-family: "Arimo", sans-serif; color: var(--red); text-align: center;
  }
  .story .lead { font-size: 21px; line-height: 1.2; }
  .story .note { font-size: 15px; line-height: 1.15; margin-top: 10px; }
  .story .claim { font-size: 21px; line-height: 1.2; margin-top: 10px; }
  .alert {
    position: absolute; left: 243px; top: 162px; width: 650px; height: 37px;
    background: var(--red); color: #fff;
    font-family: "Arimo", sans-serif; font-size: 21px;
    display: flex; align-items: center; justify-content: center;
  }
  .question {
    position: absolute; left: 243px; top: 211px; width: 650px; text-align: center;
    font-family: "Arimo", sans-serif; font-weight: 700; font-size: 18px; color: var(--ink);
  }
  .closing {
    position: absolute; left: 32px; top: 863px; width: 1136px; height: 36px;
    display: flex; align-items: center; justify-content: center;
    font-family: "Arimo", sans-serif; font-size: 21px; color: var(--red);
  }
</style>
</head>
<body>
<main class="postcard">
  <div class="frame"></div>

  <section class="hero" role="img" aria-label="Smiling portrait of candidate Mara Quill in a black blazer and pink blouse, set against grey handguns and bullets fanned out on both sides"></section>

  <h1 class="headline">Is <span class="name">Mara Quill</span> really what the <span class="name">Halverton School District</span> needs?</h1>

  <section class="details">
    <div class="mugshot" role="img" aria-label="Booking photo of the candidate's son"></div>
    <div class="husband-photo" role="img" aria-label="Photo of Simon Quill, the candidate's husband"></div>

    <div class="story">
      <p class="lead">In 2008, her son brought a gun to school.</p>
      <p class="note">Her Husband, Simon Quill while on the school board, said it<br>was an honest mistake and nothing was ever done to the child.</p>
      <p class="claim">If it were anyone else's child,<br>that child would have been expelled.</p>
    </div>

    <p class="alert">Recently her son was arrested TWICE in 1 week for theft.</p>
    <p class="question">Is this the type of person you want on your school board?</p>
  </section>

  <p class="closing">If Mara Quill cant keep her own child out of trouble, how will she ever help your children?</p>
</main>
</body>
</html>
```